I need a business card design for a new company that will be doing consulting work around issues of cultural competency, and diversity and inclusion. I would like the design to be crisp and clear with bold but conservative colors and incorporate shades of blue

Target Market(s)

Small businesses, schools, non-profits

Industry/Entity Type

Consulting

Font styles to use
Serif
Sans Serif

Colors
0c5ba6
6b449b
3276b5
0292cd

Requirements
Must have
• A Morrow Venture (name of company)
• Lemlem Tavish
• CEO
• lemlem@amorrowventure.com
• (215)483-2756

```html
<!DOCTYPE html>
<html lang="en">
<head>
<meta charset="utf-8">
<title>Wayfare Consulting — Business Card</title>
<link rel="stylesheet" href="https://fonts.googleapis.com/css2?family=Cormorant+Garamond:wght@500;600;700&display=swap">
<style>
  :root {
    --paper: #ffffff;
    --canvas: #ffffff;
    --purple: #6a3d80;
    --teal: #3a8dba;
    --sky: #4686bc;
    --slate: #4a6ba0;
    --navy: #3b528d;
    --ink: #111111;
    --shadow: rgba(0, 0, 0, 0.45);
  }
  html, body {
    margin: 0;
    padding: 0;
    width: 1200px;
    height: 1200px;
    overflow: hidden;
    background: var(--canvas);
  }
  .sheet {
    position: relative;
    width: 1200px;
    height: 1200px;
  }
  .card {
    position: absolute;
    left: 192px;
    width: 789px;
    height: 473px;
    display: block;
    filter: drop-shadow(14px 16px 12px var(--shadow));
  }
  .card--front { top: 105px; }
  .card--back  { top: 621px; }
  .card text {
    font-family: "Cormorant Garamond", Georgia, serif;
  }
  .brand-label { fill: var(--paper); font-weight: 600; }
  .person-name { fill: var(--ink); font-weight: 700; }
  .person-role { fill: var(--ink); font-weight: 500; }
  .contact-line { fill: var(--paper); font-weight: 600; }
</style>
</head>
<body>
<main class="sheet">

  <!-- Front side -->
  <svg class="card card--front" viewBox="0 0 986 591" aria-label="Card front: Wayfare Consulting">
    <rect width="986" height="591" fill="var(--paper)"/>
    <g class="facet-sweep">
      <polygon points="0,0 870,591 0,591" fill="var(--navy)"/>
      <polygon points="0,0 720,591 0,591" fill="var(--slate)"/>
      <polygon points="0,0 610,591 0,591" fill="var(--navy)"/>
      <polygon points="0,0 590,591 0,591" fill="var(--teal)"/>
    </g>
    <g class="facet-corner">
      <polygon points="640,0 986,0 986,191" fill="var(--navy)"/>
      <polygon points="720,0 986,0 986,178" fill="var(--slate)"/>
      <polygon points="800,0 986,0 986,166" fill="var(--sky)"/>
    </g>
    <path class="brand-tab" d="M401,192 H868 Q895,192 895,219 V276 H428 Q401,276 401,249 Z" fill="var(--purple)"/>
    <text class="brand-label" x="616" y="247" font-size="44" text-anchor="middle">Wayfare Consulting</text>
  </svg>

  <!-- Back side -->
  <svg class="card card--back" viewBox="0 0 986 591" aria-label="Card back: Lemlem Tavish, CEO">
    <rect width="986" height="591" fill="var(--paper)"/>
    <polygon class="contact-field" points="840,112 986,190 986,591 236,591" fill="var(--purple)"/>
    <g class="facet-corner">
      <polygon points="640,0 986,0 986,191" fill="var(--navy)"/>
      <polygon points="720,0 986,0 986,178" fill="var(--slate)"/>
      <polygon points="800,0 986,0 986,166" fill="var(--sky)"/>
    </g>
    <g class="facet-base">
      <polygon points="0,400 345,591 0,591" fill="var(--navy)"/>
      <polygon points="0,412 270,591 0,591" fill="var(--slate)"/>
      <polygon points="0,424 190,591 0,591" fill="var(--sky)"/>
    </g>
    <path class="brand-tab" d="M103,80 H492 Q519,80 519,107 V150 H130 Q103,150 103,123 Z" fill="var(--purple)"/>
    <text class="brand-label" x="311" y="127" font-size="39" text-anchor="middle">Wayfare Consulting</text>

    <text class="person-name" x="140" y="210" font-size="34">Lemlem Tavish</text>
    <text class="person-role" x="140" y="248" font-size="29">CEO</text>

    <g class="contact-icon contact-icon--mail" fill="none" stroke="var(--paper)" stroke-width="2">
      <rect x="533" y="420" width="28" height="20" fill="var(--paper)"/>
      <polyline points="533,420 547,432 561,420" stroke="var(--purple)"/>
      <polyline points="533,440 543,430 M551,430 561,440" stroke="var(--purple)"/>
    </g>
    <text class="contact-line" x="577" y="436" font-size="24">lemlem@amorrowventure.com</text>

    <g class="contact-icon contact-icon--phone">
      <circle cx="547" cy="471" r="13" fill="none" stroke="var(--paper)" stroke-width="2.2"/>
      <path d="M541,463 q2,-2 4,0 l1,3 q0,1.5 -1.5,2.2 q1.5,4 5.5,5.5 q0.8,-1.5 2.2,-1.5 l3,1 q2,2 0,4 q-3,2.5 -7,0.5 q-5,-3 -7.5,-7.5 q-2,-4 0.3,-7.2 z" fill="var(--paper)"/>
    </g>
    <text class="contact-line" x="577" y="480" font-size="24">(215)483-2756</text>
  </svg>

</main>
</body>
</html>
```